Church Grand Opening Bill Board design

I would like to create a bill board design for our church's grand opening. I would like to incorporate pictures of two separate preachers with a creative way of blending them both together so it won't take up too much space. I have included pictures and logo.

I am open for color coordination and I have included a couple of past designs to use as a reference

The information I would want on the Build Board is the following (1) Grand Opening (2) 4827 E. Pellford Street (3) 10:30am (4) Multi-Ethnic Church Planting Church (5) Sept. 26, 2021

Target Market(s)

Church shoppers and those who have never been connected to a church

Font styles to use
Serif

Requirements
Must have
• Our Logo
Nice to have
• i do not want any crosses or religious symbols

```html
<!DOCTYPE html>
<html lang="en">
<head>
<meta charset="utf-8">
<title>Kindle Church – Grand Opening Billboard</title>
<link href="https://fonts.googleapis.com/css2?family=Cinzel:wght@600;700&family=Crimson+Pro:wght@400;600;700&display=swap" rel="stylesheet">
<style>
  :root {
    --page: #d2d2d2;
    --board-light: #f7f8fb;
    --board-mid: #e4e7ee;
    --halo: #ffffff;
    --ink: #111111;
    --accent: #f4962f;
    --accent-deep: #e8861c;
  }
  * { box-sizing: border-box; margin: 0; padding: 0; }
  html, body {
    width: 977px; height: 1200px; overflow: hidden;
    background: var(--page);
  }
  .billboard {
    position: absolute; left: 20px; top: 366px;
    width: 937px; height: 467px; overflow: hidden;
    background: linear-gradient(160deg, var(--board-light) 0%, var(--board-mid) 45%, var(--board-light) 70%, var(--board-mid) 100%);
    font-family: "Crimson Pro", Georgia, serif;
    color: var(--ink);
  }
  .halo { position: absolute; border-radius: 50%; background: var(--halo); }
  .halo--left { left: -160px; top: -60px; width: 420px; height: 560px; }
  .halo--right { left: 675px; top: -50px; width: 420px; height: 560px; }
  .speaker { position: absolute; }
  .speaker--left {
    left: 0; top: 27px; width: 250px; height: 440px;
    border-radius: 110px 110px 0 0;
    background: linear-gradient(180deg, #6b5a4e 0%, #2a2a2e 22%, #5f6670 45%, #1e1f23 70%, #2b2c31 100%);
  }
  .speaker--right {
    left: 693px; top: 30px; width: 244px; height: 437px;
    border-radius: 110px 110px 0 0;
    background: linear-gradient(180deg, #5a3a2a 0%, #2a1e1c 24%, #241c1b 70%, #5c7390 100%);
  }
  .brand {
    position: absolute; left: 0; right: 0; top: 62px;
    display: flex; justify-content: center; align-items: center; gap: 12px;
  }
  .brand__dot { width: 26px; height: 26px; border-radius: 50%; background: var(--accent); }
  .brand__name {
    font-family: "Crimson Pro", Georgia, serif; font-weight: 600;
    font-size: 44px; color: var(--ink); letter-spacing: 0.5px;
  }
  .headline {
    position: absolute; left: 0; right: 0; top: 160px;
    text-align: center; font-family: "Cinzel", "Times New Roman", serif;
    font-weight: 700; line-height: 0.9; color: var(--ink);
  }
  .headline__line { display: block; }
  .headline__line--grand { font-size: 80px; letter-spacing: 1px; }
  .headline__line--opening { font-size: 80px; letter-spacing: 0; }
  .address {
    position: absolute; left: 275px; top: 329px; width: 387px; height: 42px;
    background: var(--accent);
    display: flex; align-items: center; justify-content: center; gap: 8px;
    font-weight: 700; font-size: 29px; color: var(--ink);
  }
  .address svg { width: 18px; height: 24px; }
  .details {
    position: absolute; left: 0; right: 0; top: 384px;
    display: flex; justify-content: center; align-items: center; gap: 10px;
    font-size: 20px; font-weight: 600;
  }
  .details__rule { width: 34px; height: 2px; background: var(--ink); }
  .details__date { color: var(--accent-deep); }
  .details svg { width: 24px; height: 24px; }
  .traits {
    position: absolute; left: 0; right: 0; top: 416px;
    display: flex; justify-content: center; gap: 10px;
    font-size: 19px;
  }
  .traits__item { display: flex; align-items: center; gap: 5px; }
  .traits svg { width: 16px; height: 16px; }
</style>
</head>
<body>
  <section class="billboard">
    <div class="halo halo--left"></div>
    <div class="halo halo--right"></div>
    <div class="speaker speaker--left" role="img" aria-label="Photo of the first preacher speaking with a headset microphone, in a dark jacket and grey shirt"></div>
    <div class="speaker speaker--right" role="img" aria-label="Photo of the second preacher smiling, in a black polo shirt and jeans"></div>

    <div class="brand">
      <span class="brand__dot"></span>
      <span class="brand__name">Kindle Church</span>
    </div>

    <h1 class="headline">
      <span class="headline__line headline__line--grand">GRAND</span>
      <span class="headline__line headline__line--opening">OPENING</span>
    </h1>

    <div class="address">
      <svg viewBox="0 0 18 24" aria-hidden="true"><path d="M9 0a9 9 0 0 0-9 9c0 6.5 9 15 9 15s9-8.5 9-15a9 9 0 0 0-9-9z" fill="#fff"/><circle cx="9" cy="9" r="3.5" fill="var(--accent)"/></svg>
      <span>4827 E. Pellford Street</span>
    </div>

    <div class="details">
      <span class="details__rule"></span>
      <svg viewBox="0 0 24 24" aria-hidden="true"><circle cx="12" cy="13" r="9" fill="none" stroke="var(--accent)" stroke-width="2"/><path d="M12 8v5l3 2" fill="none" stroke="var(--accent)" stroke-width="2" stroke-linecap="round"/><path d="M3 5l4-3M21 5l-4-3" stroke="var(--accent)" stroke-width="2" stroke-linecap="round"/></svg>
      <span class="details__time">10:30am</span>
      <span class="details__date">Sept. 26, 2021</span>
      <span class="details__rule"></span>
    </div>

    <div class="traits">
      <span class="traits__item"><svg viewBox="0 0 16 16" aria-hidden="true"><circle cx="8" cy="8" r="8" fill="var(--accent)"/><path d="M4.5 8.2l2.3 2.3 4.7-4.8" fill="none" stroke="#fff" stroke-width="2" stroke-linecap="round" stroke-linejoin="round"/></svg>Planting Church</span>
      <span class="traits__item"><svg viewBox="0 0 16 16" aria-hidden="true"><circle cx="8" cy="8" r="8" fill="var(--accent)"/><path d="M4.5 8.2l2.3 2.3 4.7-4.8" fill="none" stroke="#fff" stroke-width="2" stroke-linecap="round" stroke-linejoin="round"/></svg>Multi-Ethnic Church</span>
    </div>
  </section>
</body>
</html>
```